New Business Card Design Project

hello again,
i have an awful year and we were not able to complete our logo plan. we would like to use our #1 logo for business card design process. the primary colors for business card should be white background with orange & black letters. our business is mobil truck cranes. we deliver heavy stuff and unload cargo with crane that is mounted on our trucks.
here is our business card info:
HARBOR LIFT HAULERS, INC.
428 WESTCOTT AVE
MERRICK, NY 11542
OFFICE - 516 487 3091
DIRECT - 1 888 LIFT HAULS
MARK@HLHAULERS.COM
PLEASE also try to get our slogan on card .... "Our Loads Keep Rollin"
lastly please also put "24 hour Knuckleboom Service"
you can call me anytime 24/7 to discuss...my cell # is: 516 759 2036
please also list: Mark Delroy, President
Target Market(s)
Heavy Construction industry
Industry/Entity Type
heavy construction industry
Contact Information for Business Card
24 Hr Knuckleboom Service

```html
<!DOCTYPE html>
<html lang="en">
<head>
<meta charset="utf-8">
<title>Harbor Lift Haulers – Business Cards</title>
<link rel="stylesheet" href="https://fonts.googleapis.com/css2?family=Montserrat:wght@400;500;700;800&display=swap">
<style>
  :root {
    --page-bg: #9a9a9a;
    --card-bg: #ffffff;
    --orange: #f0400f;
    --ink: #2a2a2a;
    --grey: #555555;
    --skyline: #4a4a4a;
  }
  * { box-sizing: border-box; margin: 0; padding: 0; }
  html, body {
    width: 1200px; height: 800px; overflow: hidden;
    background: var(--page-bg);
    font-family: "Montserrat", sans-serif;
  }
  .stage {
    width: 1200px; height: 800px;
    display: flex; align-items: center; justify-content: center; gap: 40px;
  }
  .card {
    position: relative;
    width: 540px; height: 310px;
    background: var(--card-bg);
    border-bottom: 4px solid var(--orange);
    box-shadow: 0 10px 24px rgba(0,0,0,0.25);
    overflow: hidden;
  }

  /* Front */
  .brand {
    position: absolute; left: 34px; top: 34px;
    display: flex; align-items: center; gap: 10px;
    width: 210px;
  }
  .brand-dot {
    flex: none; width: 18px; height: 18px; border-radius: 50%;
    background: var(--orange);
  }
  .brand-name {
    font-weight: 800; font-size: 19px; line-height: 1.15;
    color: var(--ink); letter-spacing: 0.5px;
  }
  .divider {
    position: absolute; left: 250px; right: 0; top: 112px;
    height: 2px; background: var(--ink);
  }
  .person {
    position: absolute; right: 24px; top: 58px; text-align: right;
  }
  .person-name {
    color: var(--orange); font-weight: 500; font-size: 22px;
    letter-spacing: 1px; text-transform: uppercase;
  }
  .person-title { color: var(--grey); font-size: 12px; margin-top: 2px; }
  .address {
    position: absolute; right: 24px; top: 150px; text-align: right;
    font-size: 12px; line-height: 1.5; color: var(--grey);
  }
  .contacts {
    position: absolute; left: 34px; bottom: 28px;
    list-style: none; font-size: 12px; line-height: 1.7; color: var(--grey);
  }
  .contacts li { display: flex; align-items: center; gap: 8px; }
  .contacts svg { width: 11px; height: 11px; fill: var(--orange); flex: none; }

  /* Back */
  .slogan {
    position: absolute; left: 30px; top: 38px;
    font-weight: 800; font-size: 30px; letter-spacing: 0.5px;
    color: var(--ink); text-transform: uppercase;
  }
  .slogan .accent { color: var(--orange); }
  .slogan-rule {
    position: absolute; left: 30px; right: 30px; top: 84px;
    height: 1px; background: var(--orange);
  }
  .service {
    position: absolute; left: 30px; top: 92px;
    font-size: 17px; color: var(--grey); font-weight: 500;
  }
  .service strong { color: var(--orange); font-weight: 700; }
  .skyline-art {
    position: absolute; left: 0; right: 0; bottom: 0; height: 160px;
    background: linear-gradient(180deg, #ffffff 0%, #bdbdbd 45%, var(--skyline) 100%);
  }
  .skyline-line {
    position: absolute; left: 0; right: 0; bottom: 52px;
    height: 3px; background: var(--orange);
  }
</style>
</head>
<body>
<main class="stage">

  <section class="card card-front">
    <div class="brand">
      <span class="brand-dot"></span>
      <span class="brand-name">HARBOR LIFT HAULERS, INC.</span>
    </div>
    <div class="divider"></div>
    <div class="person">
      <p class="person-name">Mark Delroy</p>
      <p class="person-title">President</p>
    </div>
    <address class="address">
      Harbor Lift Haulers, Inc<br>
      428 Westcott Ave<br>
      Merrick, NY 11542
    </address>
    <ul class="contacts">
      <li>
        <svg viewBox="0 0 24 24"><path d="M6.6 10.8a15 15 0 0 0 6.6 6.6l2.2-2.2a1 1 0 0 1 1-.25 11.4 11.4 0 0 0 3.6.57 1 1 0 0 1 1 1V20a1 1 0 0 1-1 1A17 17 0 0 1 3 4a1 1 0 0 1 1-1h3.5a1 1 0 0 1 1 1c0 1.25.2 2.45.57 3.57a1 1 0 0 1-.25 1z"/></svg>
        516 487 3091
      </li>
      <li>
        <svg viewBox="0 0 24 24"><path d="M3 5h18v14H3z M3 5l9 7 9-7" fill="none" stroke="#f0400f" stroke-width="2.5"/></svg>
        1 888 LIFT HAULS
      </li>
      <li>
        <svg viewBox="0 0 24 24"><circle cx="12" cy="12" r="10"/></svg>
        Mark@HLhaulers.com
      </li>
    </ul>
  </section>

  <section class="card card-back">
    <h2 class="slogan">Our Loads Keep <span class="accent">Rollin</span></h2>
    <div class="slogan-rule"></div>
    <p class="service"><strong>24 hour</strong> Knuckleboom <strong>Service</strong></p>
    <div class="skyline-art" role="img" aria-label="Dark grey city skyline silhouette with a harbor statue, bridge and a truck-mounted knuckleboom crane"></div>
    <div class="skyline-line"></div>
  </section>

</main>
</body>
</html>
```